Velbrix SA

Découpe de métaux - Fourniture de tôles - Accessoires de machines de chantier (European Patent)

Les designs se ressemblent

Besoin de plus de jours pour examiner

• Mon projet doit comprendre la photo de la halle (bâtiment)

```html
<!DOCTYPE html>
<html lang="fr">
<head>
<meta charset="utf-8">
<title>Velbrix SA – Annonce</title>
<link href="https://fonts.googleapis.com/css2?family=Oswald:wght@300;400;500;600;700&display=swap" rel="stylesheet">
<style>
  :root {
    --stage: #5b5b5d;
    --charcoal: #2b292c;
    --charcoal-deep: #232124;
    --charcoal-veil: rgba(38, 36, 40, 0.62);
    --white: #ffffff;
    --paper: #f1f1f2;
    --paper-shade: #dcdcdf;
    --ink: #2b292c;
    --machine-dark: #2e2a35;
    --machine-violet: #5f5270;
    --machine-light: #9a8dab;
    --hall-sky: #4d6ea8;
    --hall-mountain: #6b6f6a;
    --hall-grass: #5c7a3a;
  }
  * { margin: 0; padding: 0; box-sizing: border-box; }
  html, body { width: 1200px; height: 617px; overflow: hidden; }
  body {
    background: var(--stage);
    font-family: "Oswald", "Arial Narrow", sans-serif;
    position: relative;
  }
  .ad {
    position: absolute;
    left: 402px; top: 28px;
    width: 395px; height: 560px;
    background: var(--paper);
    overflow: hidden;
    box-shadow: 0 6px 18px rgba(0,0,0,.35);
  }
  .ad > * { position: absolute; }
  .brand-column { left: 0; top: 0; width: 168px; height: 347px; background: var(--charcoal); }
  .contact-area { left: 168px; top: 0; width: 227px; height: 105px; background: linear-gradient(135deg, var(--white), var(--paper)); }
  .brand {
    left: 0; top: 40px; width: 168px;
    display: flex; align-items: center; justify-content: center; gap: 7px;
    color: var(--white); font-weight: 500; font-size: 21px; letter-spacing: .5px;
  }
  .brand-dot { width: 12px; height: 12px; border-radius: 50%; background: var(--white); }
  .contact {
    left: 234px; width: 131px; height: 23px;
    background: var(--charcoal-deep); color: var(--white);
    display: flex; align-items: center; gap: 5px; padding-left: 11px;
    font-size: 11.5px; font-weight: 400; letter-spacing: .2px;
    white-space: nowrap;
  }
  .contact svg { width: 10px; height: 10px; flex: none; }
  .contact--web { top: 27px; }
  .contact--mail { top: 57px; }
  .machine-photo {
    left: 168px; top: 105px; width: 227px; height: 242px;
    background: radial-gradient(circle at 62% 58%, var(--machine-light) 0%, var(--machine-violet) 42%, var(--machine-dark) 88%);
  }
  .headline-block {
    left: 33px; top: 136px; width: 190px; height: 181px;
    border: 1px solid var(--white);
    background: var(--charcoal-veil);
    padding: 13px 0 0 19px;
    color: var(--white);
  }
  .headline {
    font-weight: 700; font-size: 29px; line-height: 35px;
    letter-spacing: 0; white-space: nowrap;
  }
  .headline + .headline { margin-top: 16px; }
  .lower-section { left: 0; top: 347px; width: 395px; height: 166px; background: linear-gradient(120deg, var(--white) 30%, var(--paper) 65%, var(--paper-shade)); }
  .hall-frame { left: 33px; top: 364px; width: 188px; height: 149px; background: var(--charcoal); }
  .hall-photo {
    left: 51px; top: 381px; width: 154px; height: 116px;
    background: linear-gradient(180deg, var(--hall-sky) 0%, var(--hall-mountain) 35%, var(--paper-shade) 55%, var(--hall-grass) 100%);
  }
  .accessories {
    left: 245px; top: 390px; color: var(--ink);
    font-weight: 400; font-size: 21px; line-height 24px; line-height: 24px;
    white-space: nowrap;
  }
  .accessories-rule { left: 246px; top: 465px; width: 124px; height: 1px; background: var(--ink); }
  .patent { left: 245px; top: 477px; color: var(--ink); font-weight: 400; font-size: 15px; white-space: nowrap; }
  .call-bar {
    left: 0; top: 513px; width: 395px; height: 47px;
    background: var(--charcoal); color: var(--white);
    display: flex; align-items: center; justify-content: center; gap: 8px;
    font-weight: 500; font-size: 28px; letter-spacing: .3px; white-space: nowrap;
  }
  .call-bar svg { width: 26px; height: 26px; flex: none; }
</style>
</head>
<body>
  <div class="ad">
    <div class="brand-column"></div>
    <div class="contact-area"></div>
    <div class="brand"><span class="brand-dot"></span>Velbrix SA</div>

    <div class="contact contact--web">
      <svg viewBox="0 0 20 20" fill="none" stroke="#fff" stroke-width="1.6"><circle cx="10" cy="10" r="8.5"/><ellipse cx="10" cy="10" rx="3.8" ry="8.5"/><path d="M1.5 10h17M3 5.5h14M3 14.5h14"/></svg>
      WWW.VELBRIX.CH
    </div>
    <div class="contact contact--mail">
      <svg viewBox="0 0 20 20" fill="none" stroke="#fff" stroke-width="1.6"><rect x="1.5" y="4" width="17" height="12"/><path d="M1.5 4l8.5 7 8.5-7"/></svg>
      INFO@VELBRIX.CH
    </div>

    <div class="machine-photo" role="img" aria-label="Tête de découpe laser d'une machine de découpe de métaux"></div>

    <div class="headline-block">
      <h1 class="headline">DÉCOUPE<br>DE MÉTAUX</h1>
      <h2 class="headline">FOURNITURE<br>DE TÔLES</h2>
    </div>

    <div class="lower-section"></div>
    <div class="hall-frame"></div>
    <div class="hall-photo" role="img" aria-label="Halle de l'entreprise, bâtiment blanc devant les montagnes"></div>

    <p class="accessories">ACCESSOIRES<br>DE MACHINES DE<br>CHANTIER</p>
    <div class="accessories-rule"></div>
    <p class="patent">(European Patent)</p>

    <div class="call-bar">
      CALL US NOW
      <svg viewBox="0 0 26 26" fill="none" stroke="#fff" stroke-width="1.8"><circle cx="13" cy="13" r="11.5"/><path d="M9.5 7.5l2 3-1.3 1.3c.8 1.7 2 2.9 3.9 3.9l1.3-1.3 3 2-1.2 2c-4.5-.3-8.6-4.4-8.9-8.9z" fill="#fff" stroke-width="1"/></svg>
      027/555.41.60
    </div>
  </div>
</body>
</html>
```